Bright Harbour Charity - helping the disadvantaged

I would like a new web site design for my charity BRIGHT HARBOUR. The charity provides help for the disadvantaged. See current site
brightharbour.org.au for details. Please refer to the current site for information on the charity. The objectives of the charity are in the "about us" tab. You will also notice on the site that we provide information about events that we sponsor an area for this should be provided on the site.

Target Market(s)

We have two targets:
1. Individuals and Businesses that will donate money to the charity.
2. Individuals that are in need of support from the charity.

Industry/Entity Type

Charity

Requirements
Must have
• Ability for individuals to be able to understand the type of support we can provide.
Nice to have
• Our logo should be prominate on each pages
Should not have
• Should be use modern fonts

```html
<!DOCTYPE html>
<html lang="en">
<head>
<meta charset="utf-8">
<title>Bright Harbour</title>
<link href="https://fonts.googleapis.com/css2?family=PT+Sans:wght@400;700&family=Delius&display=swap" rel="stylesheet">
<style>
:root{
  --sky-top:#7cc3f3;
  --sky-mid:#c9e7fb;
  --grass-light:#cfe88f;
  --grass:#9acb45;
  --magenta:#b0196f;
  --magenta-light:#e05aa6;
  --magenta-dark:#8a0f55;
  --heading:#5a0a30;
  --body:#4a1030;
  --logo-green:#5a9e1f;
  --gold:#f5b342;
  --yellow:#ffd21f;
  --orange:#f28a0c;
  --green:#1f8a2a;
  --green-dark:#0b5a1a;
}
*{margin:0;padding:0;box-sizing:border-box}
html,body{width:1200px;height:1013px;overflow:hidden}
body{position:relative;font-family:"PT Sans",sans-serif;color:var(--body)}
.backdrop{position:absolute;inset:0;
  background:linear-gradient(180deg,var(--sky-top) 0%,var(--sky-mid) 40%,#eef8fd 62%,var(--grass-light) 80%,var(--grass) 100%)}
.logo{position:absolute;left:0;width:1200px;top:56px;display:flex;justify-content:center;align-items:center;gap:12px}
.logo-dot{width:22px;height:22px;border-radius:50%;background:var(--gold)}
.logo-name{font-size:40px;font-weight:400;color:var(--logo-green);letter-spacing:1px;line-height:44px}
.frame{position:absolute;left:150px;top:167px;width:873px;height:720px;border-radius:12px;
  background:linear-gradient(90deg,var(--magenta-dark),var(--magenta) 40%,var(--magenta) 60%,var(--magenta-dark))}
.frame-inner{position:absolute;left:8px;right:8px;top:8px;bottom:12px;border-radius:8px;background:#fff}
.nav{position:absolute;left:162px;top:172px;width:849px;height:40px;border-radius:10px;
  background:linear-gradient(180deg,var(--magenta-light),var(--magenta) 55%,var(--magenta-dark));display:flex;align-items:center;justify-content:space-around;padding:0 20px}
.nav a{color:#fff;text-decoration:none;font-size:13px;text-shadow:0 1px 1px rgba(0,0,0,.5)}
.tab{position:absolute;left:170px;top:222px;width:222px;height:27px;border-radius:6px 6px 0 0;
  background:linear-gradient(180deg,var(--magenta-light),var(--magenta));color:#fff;font-size:17px;line-height:26px;padding:0 12px}
.intro{position:absolute;left:184px;top:270px;width:405px;font-size:11.5px;line-height:14.5px}
.intro h2{font-size:13px;font-weight:400;color:var(--heading);letter-spacing:.3px;margin-bottom:14px}
.intro p{margin-bottom:14px}
.intro ul{list-style:none;margin-bottom:14px}
.intro li{text-indent:15px}
.rule{position:absolute;left:186px;top:579px;width:346px;border-top:1px solid #ddd}
.news{position:absolute;left:188px;top:610px;width:400px;font-size:11.5px;line-height:14.5px}
.news h3{font-size:13px;font-weight:700;color:var(--heading);margin-bottom:14px}
.more{position:absolute;left:186px;top:704px;width:70px;height:23px;border-radius:12px;background:#b45a92;color:#fff;font-size:11px;text-align:center;line-height:23px}
.poster-back{position:absolute;left:614px;top:222px;width:390px;height:200px;background:#2a6fb8;transform:rotate(3deg)}
.poster{position:absolute;left:644px;top:229px;width:351px;height:180px;
  background:linear-gradient(180deg,#bfe7fb,#e9f7ff 55%,#9fd46a)}
.donate-btn{position:absolute;left:698px;top:459px;width:222px;height:28px;border-radius:8px 8px 0 0;
  background:linear-gradient(180deg,var(--magenta-light),var(--magenta));color:#fff;font-family:"Delius",cursive;font-size:21px;text-align:center;line-height:28px}
.kids{position:absolute;left:604px;top:519px;width:396px;height:233px;
  background:linear-gradient(90deg,#8fb8d6,#f2d3c2 40%,#e86aa0 65%,#7e9a4a)}
.card{position:absolute;top:757px;width:202px;height:111px;border-radius:8px;border:1px solid rgba(255,255,255,.8);box-shadow:0 0 0 1px rgba(0,0,0,.12);color:#222;padding:8px 10px 0 76px}
.card h4{font-family:"Delius",cursive;font-weight:400;font-size:18px;margin-bottom:4px}
.card p{font-size:11.5px;line-height:14.5px}
.card svg{position:absolute;left:24px;top:12px}
.card-donate{left:167px;background:linear-gradient(180deg,var(--yellow),var(--orange))}
.card-donate h4{color:#5a3a00}
.card-goal{left:379px;background:linear-gradient(180deg,#8dd35a,var(--green) 45%,var(--green-dark));color:#fff}
.card-goal h4{color:#eaffd0}
.card-directors{left:593px;background:linear-gradient(180deg,#f4a3d0,var(--magenta-light) 40%,var(--magenta-dark));color:#fff}
.card-contact{left:806px;background:linear-gradient(180deg,#ffb02e,var(--orange));color:#fff}
.card-contact h4,.card-directors h4{color:#fff}
</style>
</head>
<body>
<div class="backdrop" role="img" aria-label="Sky with clouds above rolling green hills"></div>

<header class="logo">
  <span class="logo-dot"></span>
  <span class="logo-name">BRIGHT HARBOUR</span>
</header>

<div class="frame"><div class="frame-inner"></div></div>
<nav class="nav">
  <a href="#">Home</a><a href="#">About Us</a><a href="#">Donate</a><a href="#">Apply</a><a href="#">Pledge</a><a href="#">Nominate</a><a href="#">Events</a><a href="#">Contact Us</a><a href="#">Directors</a>
</nav>

<div class="tab">Welcome to Bright Harbour</div>

<section class="intro">
  <h2>OBJECTIVES</h2>
  <p>The objective for Bright Harbour is to provide direct assistance to people in need in Australia</p>
  <p>Providing direct assistance includes the following:</p>
  <ul>
    <li>making loans to people in need;</li>
    <li>providing training and education to people in need;</li>
    <li>providing accommodation for people in medical care and their carers and families;</li>
    <li>providing food to people in need; and</li>
    <li>providing cash payments to people in need</li>
  </ul>
  <h2>PEOPLE IN NEED</h2>
  <p>People in need includes orphaned children, disabled people, people living under poverty, distress, misfortune or destitution, people suffering from sickness, and also Aboriginals and Torres Strait Islanders .</p>
</section>
<div class="rule"></div>
<section class="news">
  <h3>Harmony Day Saturday 24th March 2012 10am – 3pm</h3>
  <p>Bright Harbour &amp; Linwood Care will be holding a multicultural market and art exhibition combined with a community harmony day being held on site at.... Linwood Care Education Centre 15 – 17 Kellerman Road, Ashvale</p>
</section>
<a class="more">more</a>

<div class="poster-back"></div>
<div class="poster" role="img" aria-label="Harmony Day event poster, photo gallery"></div>

<div class="donate-btn">Donate Now</div>
<div class="kids" role="img" aria-label="Photo of a group of smiling children"></div>

<article class="card card-donate">
  <svg width="34" height="30" viewBox="0 0 34 30" aria-hidden="true"><path d="M17 28 L3 14 A7 7 0 0 1 17 6 A7 7 0 0 1 31 14Z" fill="#e0452a"/></svg>
  <h4>Donate now</h4>
  <p>Lorem ipsum ea sit clita definiebas, cum vidit zzril necessitati-bus eubus ration</p>
</article>
<article class="card card-goal">
  <svg width="30" height="30" viewBox="0 0 30 30" aria-hidden="true"><circle cx="15" cy="15" r="13" fill="#fff"/><circle cx="15" cy="15" r="9" fill="#d8262a"/><circle cx="15" cy="15" r="5" fill="#fff"/><circle cx="15" cy="15" r="2" fill="#d8262a"/></svg>
  <h4>Our Goal</h4>
  <p>Lorem ipsum ea sit clita definiebas, cum vidit zzril necessitati-bus eubus ration</p>
</article>
<article class="card card-directors">
  <svg width="40" height="36" viewBox="0 0 40 36" aria-hidden="true"><circle cx="13" cy="9" r="6" fill="#f2c9a0"/><rect x="4" y="16" width="18" height="16" rx="6" fill="#3a5a8a"/><circle cx="28" cy="13" r="6" fill="#f2c9a0"/><rect x="19" y="20" width="18" height="14" rx="6" fill="#7a2a4a"/></svg>
  <h4>Directors</h4>
  <p>Lorem ipsum ea sit clita definiebas, cum vidit zzril necessitati-bus eubus ration</p>
</article>
<article class="card card-contact">
  <svg width="40" height="32" viewBox="0 0 40 32" aria-hidden="true"><path d="M2 10 Q20 -2 38 10 L34 15 L27 12 L27 8 Q20 5 13 8 L13 12 L6 15Z" fill="#3a8fd0"/><rect x="9" y="14" width="22" height="16" rx="4" fill="#3a8fd0"/><circle cx="20" cy="22" r="5" fill="#fff"/></svg>
  <h4>Contact Us</h4>
  <p>Lorem ipsum ea sit clita definiebas, cum vidit zzril necessitati-bus eubus ration</p>
</article>
</body>
</html>
```